Gift Voucher For Medical Cosmetic Clinic

I need a high end, beautiful gift voucher for my Cosmetic Medical Clinic that I will provide to customers in a beautifully designed envelope. I like the colours blue with different tones of blue, white and silver. I have attached my business card for further information.
The address is: 3/14 Dunmore Lane, Ferrymead, Christchurch 8023.
Phone: 0800-457-839
Email: mirel@tovanu.co.nz
Website: www.tovanu.co.nz

```html
<!DOCTYPE html>
<html lang="en">
<head>
<meta charset="UTF-8">
<title>Tovanu Gift Voucher</title>
<link rel="stylesheet" href="https://fonts.googleapis.com/css2?family=EB+Garamond:wght@400;500&family=Montserrat:wght@200;500;600;700&display=swap">
<style>
  :root {
    --silver-light: #ffffff;
    --silver-mid: #e4e5e8;
    --silver-dark: #b9bcc2;
    --brand-blue: #1f6db3;
    --navy: #16275e;
    --cyan: #4cc4ec;
    --sky: #36a2dc;
    --mid-blue: #2f7fc9;
    --deep-blue: #2b58ad;
    --white: #ffffff;
  }
  html, body {
    margin: 0;
    padding: 0;
    overflow: hidden;
    background: #ffffff;
  }
  .voucher {
    position: relative;
    width: 1200px;
    height: 866px;
    overflow: hidden;
    font-family: "EB Garamond", Georgia, serif;
  }
  .voucher-background {
    position: absolute;
    inset: 0;
    width: 1200px;
    height: 866px;
  }
  .brand {
    position: absolute;
    left: 96px;
    top: 340px;
    width: 330px;
    text-align: center;
  }
  .brand-ring {
    position: absolute;
    left: 190px;
    top: 150px;
    width: 170px;
    height: 170px;
    border-radius: 50%;
    border: 4px solid var(--silver-dark);
    box-sizing: border-box;
  }
  .brand-name {
    margin: 0;
    font-family: "EB Garamond", Georgia, serif;
    font-weight: 400;
    font-size: 92px;
    line-height: 1;
    letter-spacing: 2px;
    color: var(--brand-blue);
  }
  .treatments {
    position: absolute;
    left: 98px;
    top: 553px;
    margin: 0;
    padding: 0 0 0 22px;
    font-size: 24px;
    line-height: 33px;
    color: var(--brand-blue);
  }
  .treatments li::marker {
    font-size: 18px;
  }
  .value-badge {
    position: absolute;
    left: 806px;
    top: 77px;
    width: 240px;
    height: 240px;
  }
  .value-text {
    position: absolute;
    left: 806px;
    top: 160px;
    width: 240px;
    text-align: center;
    font-family: "Montserrat", Arial, sans-serif;
    color: var(--navy);
  }
  .value-amount {
    display: block;
    font-weight: 700;
    font-size: 84px;
    line-height: 0.9;
    letter-spacing: -2px;
  }
  .value-amount .currency {
    font-size: 48px;
    vertical-align: 26px;
    font-weight: 600;
    margin-right: 2px;
  }
  .value-label {
    display: block;
    font-weight: 500;
    font-size: 24px;
    letter-spacing: 1px;
    margin-top: 2px;
  }
  .voucher-title {
    position: absolute;
    right: 100px;
    top: 410px;
    margin: 0;
    text-align: right;
    font-family: "Montserrat", Arial, sans-serif;
    color: var(--white);
    line-height: 1;
  }
  .voucher-title .title-gift {
    display: block;
    font-weight: 200;
    font-size: 150px;
    letter-spacing: 6px;
    margin-right: -6px;
  }
  .voucher-title .title-voucher {
    display: block;
    font-weight: 600;
    font-size: 88px;
    letter-spacing: 2px;
    margin-top: 6px;
  }
  .voucher-terms {
    position: absolute;
    left: 457px;
    top: 704px;
    width: 660px;
    margin: 0;
    font-family: "Montserrat", Arial, sans-serif;
    font-weight: 500;
    font-size: 19.5px;
    line-height: 26px;
    color: var(--white);
  }
</style>
</head>
<body>
<main class="voucher">
  <svg class="voucher-background" viewBox="0 0 1200 866" aria-hidden="true">
    <defs>
      <linearGradient id="blue-field" x1="0" y1="0" x2="1" y2="1">
        <stop offset="0" stop-color="#3aa7df"/>
        <stop offset="0.5" stop-color="#2f7fc9"/>
        <stop offset="1" stop-color="#2b58ad"/>
      </linearGradient>
      <linearGradient id="cyan-wave" x1="0" y1="0" x2="1" y2="0">
        <stop offset="0" stop-color="#56c9ef"/>
        <stop offset="1" stop-color="#2f9bd9"/>
      </linearGradient>
      <linearGradient id="deep-wave" x1="0" y1="0" x2="1" y2="1">
        <stop offset="0" stop-color="#3b86cf"/>
        <stop offset="1" stop-color="#2a4fa6"/>
      </linearGradient>
      <linearGradient id="silver-field" x1="0" y1="0" x2="1" y2="0.4">
        <stop offset="0" stop-color="#f3f3f5"/>
        <stop offset="0.45" stop-color="#ffffff"/>
        <stop offset="0.8" stop-color="#dcdde1"/>
        <stop offset="1" stop-color="#c4c6cb"/>
      </linearGradient>
      <radialGradient id="badge-silver" cx="0.4" cy="0.35" r="0.7">
        <stop offset="0" stop-color="#ffffff"/>
        <stop offset="0.6" stop-color="#d6d7db"/>
        <stop offset="1" stop-color="#a9acb2"/>
      </radialGradient>
    </defs>

    <rect class="field-blue" width="1200" height="866" fill="url(#blue-field)"/>
    <path class="wave-upper" d="M560 0 L1200 0 L1200 40 C1050 90 900 60 760 170 C660 250 620 330 560 380 Z" fill="url(#cyan-wave)" opacity="0.85"/>
    <path class="wave-deep" d="M1200 0 L1200 560 C1100 430 1000 330 880 300 C980 180 1080 60 1200 0 Z" fill="url(#deep-wave)" opacity="0.9"/>
    <path class="wave-middle" d="M520 520 C700 430 900 420 1200 620 L1200 760 C960 560 760 540 520 640 Z" fill="#4ec3ea" opacity="0.75"/>
    <path class="wave-lower" d="M480 866 C640 760 880 700 1200 800 L1200 866 Z" fill="#3fb4e6" opacity="0.9"/>
    <path class="wave-lower-deep" d="M700 866 C860 800 1050 790 1200 830 L1200 866 Z" fill="#2a6cbf" opacity="0.7"/>

    <path class="field-silver" d="M0 0 L830 0 C690 40 600 140 565 280 C530 420 520 560 470 700 C450 760 440 820 434 866 L0 866 Z" fill="url(#silver-field)"/>
    <path class="silver-sheen" d="M0 520 C150 470 330 520 500 600 L520 560 C350 480 170 430 0 470 Z" fill="#ffffff" opacity="0.5"/>
  </svg>

  <div class="brand-ring" aria-hidden="true"></div>
  <div class="brand">
    <h1 class="brand-name">TOVANU</h1>
  </div>

  <ul class="treatments">
    <li>Dermal Injectables</li>
    <li>Plasma Facials</li>
    <li>Microneedling</li>
    <li>Skin Boosters</li>
    <li>Excessive Sweating</li>
  </ul>

  <svg class="value-badge" viewBox="0 0 240 240" aria-hidden="true">
    <circle cx="120" cy="120" r="108" fill="none" stroke="#c9cbd0" stroke-width="20" stroke-dasharray="7 6"/>
    <circle cx="120" cy="120" r="106" fill="url(#badge-silver)"/>
  </svg>
  <div class="value-text">
    <span class="value-amount"><span class="currency">$</span>100</span>
    <span class="value-label">VALUE</span>
  </div>

  <h2 class="voucher-title">
    <span class="title-gift">GIFT</span>
    <span class="title-voucher">VOUCHER</span>
  </h2>

  <p class="voucher-terms">Lorem ipsum dolor sit amet, consectetur adipiscing elit. Morbi ultricies molestie orci. Aenean purus mauris, sodales nec diam dignissim, porttitor laoreet enim. Aliquam id sollicitudin turpis.</p>
</main>
</body>
</html>
```